Brightwire Hollow Business cards

one side I would like my logo (uploaded) and the other side I want my details. I'm an electrician in sydney. The logo side I'm happy with just a white background and our logo in the middle.

Details for other side
24/7 Sydney Electrician
Marcus Pell
0431 587 219
marcus@brightwirehollow.com.au
brightwirehollow.com.au
icons for facebook, instagram, linked in

Industry/Entity Type

electrician

Contact Information for Business Card

company info

```html
<!DOCTYPE html>
<html lang="en">
<head>
<meta charset="utf-8">
<title>Brightwire Hollow Business Cards</title>
<link rel="stylesheet" href="https://fonts.googleapis.com/css2?family=Lato:wght@400;700;900&display=swap">
<style>
  :root {
    --stage: #8e8e8e;
    --brand-red: #ee3226;
    --paper: #ffffff;
    --ink: #111111;
  }
  * { margin: 0; padding: 0; box-sizing: border-box; }
  html, body { width: 1200px; height: 1200px; overflow: hidden; }
  body {
    background: var(--stage);
    font-family: "Lato", Arial, sans-serif;
    position: relative;
  }
  .card {
    position: absolute;
    left: 250px;
    width: 700px;
    height: 400px;
    box-shadow: 0 2px 6px rgba(0,0,0,0.18);
    overflow: hidden;
  }
  .card--details {
    top: 170px;
    background: var(--brand-red);
    border-radius: 24px 200px 200px 24px / 24px 200px 200px 24px;
    color: var(--paper);
  }
  .card--logo {
    top: 630px;
    background: var(--paper);
    border-radius: 200px 24px 24px 200px / 200px 24px 24px 200px;
  }
  .person-name {
    position: absolute;
    left: 44px;
    font-weight: 700;
    font-size: 29px;
    letter-spacing: 0.2px;
    line-height: 1;
    white-space: nowrap;
  }
  .contact-line {
    position: absolute;
    left: 45px;
    display: flex;
    align-items: center;
    font-size: 16px;
    letter-spacing: 0.3px;
    line-height: 1;
    white-space: nowrap;
  }
  .contact-line svg {
    width: 14px;
    height: 14px;
    margin-right: 14px;
    flex: none;
  }
  .social-row {
    position: absolute;
    left: 45px;
    top: 332px;
    display: flex;
    gap: 3px;
  }
  .social-dot {
    width: 21px;
    height: 21px;
    border-radius: 50%;
    background: var(--paper);
  }
  .tagline-badge {
    position: absolute;
    left: 387px;
    top: 86px;
    width: 230px;
    height: 230px;
    border-radius: 50%;
    background: var(--paper);
    color: var(--ink);
    display: flex;
    flex-direction: column;
    align-items: center;
    justify-content: center;
    text-align: center;
    line-height: 1;
  }
  .tagline-hours { font-size: 53px; font-weight: 400; }
  .tagline-city { font-size: 31px; font-weight: 400; margin-top: 2px; }
  .tagline-trade { font-size: 19.5px; font-weight: 400; margin-top: 4px; letter-spacing: 0.2px; }
  .brand-name {
    position: absolute;
    inset: 0;
    display: flex;
    flex-direction: column;
    align-items: center;
    justify-content: center;
    color: var(--brand-red);
    font-weight: 900;
    font-size: 54px;
    line-height: 1.05;
    text-transform: uppercase;
    letter-spacing: 1px;
  }
</style>
</head>
<body>
  <section class="card card--details">
    <h2 class="person-name" style="top:40px;">MARCUS PELL</h2>
    <p class="contact-line" style="top:76px;">
      <svg viewBox="0 0 14 14"><rect x="3" y="1" width="8" height="12" rx="1.5" fill="none" stroke="#fff" stroke-width="1.6"/><circle cx="7" cy="11" r="0.9" fill="#fff"/></svg>0438 216 705</p>
    <p class="contact-line" style="top:99px;">
      <svg viewBox="0 0 14 14"><rect x="1" y="3" width="12" height="8" fill="#fff"/><path d="M1 3 L7 8 L13 3" fill="none" stroke="#ee3226" stroke-width="1"/></svg>marcus@brightwirehollow.com.au</p>

    <h2 class="person-name" style="top:141px;">OWEN LACEY</h2>
    <p class="contact-line" style="top:177px;">
      <svg viewBox="0 0 14 14"><rect x="3" y="1" width="8" height="12" rx="1.5" fill="none" stroke="#fff" stroke-width="1.6"/><circle cx="7" cy="11" r="0.9" fill="#fff"/></svg>0457 392 640</p>
    <p class="contact-line" style="top:200px;">
      <svg viewBox="0 0 14 14"><rect x="1" y="3" width="12" height="8" fill="#fff"/><path d="M1 3 L7 8 L13 3" fill="none" stroke="#ee3226" stroke-width="1"/></svg>owen@brightwirehollow.com.au</p>

    <p class="contact-line" style="top:243px;">
      <svg viewBox="0 0 14 14"><path d="M3 1.5 L5.5 4 L4.2 5.8 Q5.5 8.5 8.2 9.8 L10 8.5 L12.5 11 L10.8 12.7 Q5.5 12 1.3 3.2 Z" fill="#fff"/></svg>0431 587 219</p>
    <p class="contact-line" style="top:266px;">
      <svg viewBox="0 0 14 14"><rect x="1" y="3" width="12" height="8" fill="#fff"/><path d="M1 3 L7 8 L13 3" fill="none" stroke="#ee3226" stroke-width="1"/></svg>services@brightwirehollow.com</p>
    <p class="contact-line" style="top:289px;">
      <svg viewBox="0 0 14 14"><circle cx="7" cy="7" r="6" fill="#fff"/><path d="M1 7 H13 M7 1 Q3.5 7 7 13 M7 1 Q10.5 7 7 13" fill="none" stroke="#ee3226" stroke-width="0.9"/></svg>brightwirehollow.com.au</p>

    <div class="social-row">
      <span class="social-dot"></span>
      <span class="social-dot"></span>
      <span class="social-dot"></span>
    </div>

    <div class="tagline-badge">
      <span class="tagline-hours">24/7</span>
      <span class="tagline-city">SYDNEY</span>
      <span class="tagline-trade">ELECTRICIAN</span>
    </div>
  </section>

  <section class="card card--logo">
    <div class="brand-name">
      <span>Brightwire</span>
      <span>Hollow</span>
    </div>
  </section>
</body>
</html>
```